Pathways to Brightmoor Land Ventures

size of the ad - 8”x 10.75" plus 0.25" bleed
I would like an ad for a magazine that will stand out and make people want to read the ad.
The ad should not be crowded and people reading the ad will be able to read the text.
I would like it to be a creative and modern-day design.
the list of topics should not be the focus of the ad.
the text is attached.
If you decide to use people in the ad then please no ladies.
please note that leave over 1 inch for the bottom of the footer

```html
<!DOCTYPE html>
<html lang="en">
<head>
<meta charset="UTF-8">
<title>Real Estate Course — Magazine Ad</title>
<link rel="stylesheet" href="https://fonts.googleapis.com/css2?family=Bebas+Neue&family=Yellowtail&family=Barlow:wght@500&display=swap">
<style>
  :root {
    --backdrop: #e4e4e4;
    --page: #151515;
    --page-edge: #1d1d1d;
    --ink-dark: #1f1f1f;
    --accent-red: #e01f26;
    --text-light: #f2f2f2;
    --text-soft: #d8d8d8;
    --sky-top: #a9c3d6;
    --sky-bottom: #cfdbe3;
    --facade: #e9ecef;
  }
  * { margin: 0; padding: 0; box-sizing: border-box; }
  html, body {
    width: 1200px; height: 818px; overflow: hidden;
    background: var(--backdrop);
  }
  .canvas {
    position: relative; width: 1200px; height: 818px;
    display: flex; align-items: center; justify-content: center;
  }
  .ad-page {
    position: relative; width: 590px; height: 790px;
    background: linear-gradient(135deg, var(--page-edge), var(--page) 60%);
    box-shadow: 0 8px 30px rgba(0,0,0,0.25);
    overflow: hidden;
  }
  .masthead {
    position: absolute; left: 80px; top: 34px;
    display: flex; align-items: baseline; gap: 10px;
  }
  .masthead-title {
    font-family: "Bebas Neue", sans-serif; font-size: 38px;
    color: var(--text-light); letter-spacing: 0.5px;
  }
  .masthead-script {
    font-family: "Yellowtail", cursive; font-size: 40px;
    color: var(--text-light);
  }
  .grad-cap { position: absolute; left: 388px; top: 36px; width: 88px; height: 48px; }
  .hero-photo {
    position: absolute; left: 80px; top: 82px; width: 432px; height: 452px;
    background:
      linear-gradient(200deg, transparent 0 38%, var(--facade) 38% 100%),
      linear-gradient(180deg, var(--sky-top), var(--sky-bottom));
  }
  .schedule {
    position: absolute; left: 96px; top: 390px;
    font-family: "Bebas Neue", sans-serif; font-size: 40px; line-height: 42px;
    color: var(--ink-dark);
  }
  .schedule .schedule-days { color: var(--accent-red); }
  .scholarship-note {
    position: absolute; left: 549px; top: 330px;
    transform: translate(-50%, -50%) rotate(-90deg);
    font-family: "Barlow", sans-serif; font-size: 10px; letter-spacing: 2.6px;
    color: var(--text-light); white-space: nowrap;
  }
  .offer {
    position: absolute; left: 0; right: 0; top: 576px; text-align: center;
    font-family: "Bebas Neue", sans-serif; font-size: 23px; line-height: 29px;
    letter-spacing: 1px; color: var(--text-soft);
  }
  .topics {
    position: absolute; left: 0; right: 0; top: 658px; text-align: center;
    font-family: "Barlow", sans-serif; font-size: 9.5px; line-height: 17px;
    letter-spacing: 0.6px; color: var(--text-soft);
  }
</style>
</head>
<body>
<div class="canvas">
  <section class="ad-page">
    <header class="masthead">
      <span class="masthead-title">Real Estate</span>
      <span class="masthead-script">Course</span>
    </header>
    <svg class="grad-cap" viewBox="0 0 88 48" aria-hidden="true">
      <polygon points="44,2 86,16 44,30 2,16" fill="#e01f26"/>
      <path d="M20 22 L20 40 Q44 48 68 40 L68 22 L44 30 Z" fill="#e01f26"/>
      <line x1="6" y1="18" x2="6" y2="40" stroke="#e01f26" stroke-width="2"/>
      <rect x="4" y="38" width="4" height="8" fill="#e01f26"/>
    </svg>

    <div class="hero-photo" role="img" aria-label="Photo of a modern white multi-storey building against a pale blue sky"></div>

    <div class="schedule">
      <div>Starting Feb.28</div>
      <div class="schedule-days">Monday 10 AM &nbsp;- Tuesday</div>
      <div>Evenings Sessions</div>
    </div>

    <div class="scholarship-note">LIMITED PARTIAL SCHOLARSHIPS</div>

    <div class="offer">
      <div>Early bird special for those that</div>
      <div>started or would like to go into real estate</div>
    </div>

    <div class="topics">
      <div>Partial listing &nbsp;| &nbsp;Real estate investment strategies &nbsp;| &nbsp;Due diligence</div>
      <div>Financing &nbsp;| &nbsp;Underwriting &nbsp;| &nbsp;Property management &nbsp;| &nbsp;Real estate Legal basics</div>
      <div>Sourcing deals &nbsp;| &nbsp;Syndication &nbsp;| &nbsp;Dealing with brokers &nbsp;| &nbsp;Tax fundamentals</div>
    </div>
  </section>
</div>
</body>
</html>
```